Minimalist- A clean spacious and crisp design for a Security Consulting Company

I need a design for a security consultant that deals with the upper end of town for security design, including CCTV and other electronic design. I need it to look spacious and be very simplistic in design. I want to keep it looking like Plonka or VANTU's website. I have experience in business intelligence. and have a lot of high end clients in the diamond industry and mining. My key area of income is consulting and taking them from normal to excellent security.
Target Market(s)
People interested in doing business with me
Industry/Entity Type
Electronic
Coding
Coded - Design and coding required
Number of Pages Required
4 page
Requirements
Must have
- The least amount of text possible
- A simple and nice front page with the logo.
- A contact us button
- Specialised projects button
- About us button
- Business intelligence button
Should not have
- Cluttered un-useful information

```html
<!DOCTYPE html>
<html lang="en">
<head>
<meta charset="utf-8">
<title>Halvern Strategy — Strategic &amp; Operational Plan</title>
<link rel="stylesheet" href="https://fonts.googleapis.com/css2?family=Cinzel:wght@400;600;700&family=Raleway:wght@400;500&display=swap">
<style>
  :root {
    --ink: #111111;
    --black: #000000;
    --nav: #121212;
    --red: #a80d0d;
    --red-dark: #a00000;
    --grey-photo-a: #8a8c8f;
    --grey-photo-b: #4d4f53;
    --white: #ffffff;
    --icon: #3b3f47;
  }
  * { margin: 0; padding: 0; box-sizing: border-box; }
  html, body { width: 1200px; height: 1170px; overflow: hidden; background: var(--white); }
  body { position: relative; font-family: "Raleway", sans-serif; color: var(--ink); }

  .site-header { position: absolute; top: 0; left: 0; width: 1200px; height: 81px; display: flex; align-items: center; justify-content: center; }
  .brand { display: flex; align-items: center; gap: 10px; }
  .brand-mark { width: 36px; height: 36px; background: var(--red); }
  .brand-name { font-family: "Cinzel", serif; font-weight: 700; font-size: 24px; color: var(--ink); letter-spacing: 0.5px; }

  .main-nav { position: absolute; top: 81px; left: 0; width: 1200px; height: 42px; background: var(--nav);
    display: flex; justify-content: center; gap: 8px; }
  .main-nav a { height: 42px; line-height: 42px; padding: 0 18px; font-family: "Cinzel", serif; font-size: 13px;
    color: var(--white); text-decoration: none; letter-spacing: 0.3px; white-space: nowrap; }
  .main-nav a.is-active { background: var(--red); padding: 0 22px; }

  .hero { position: absolute; top: 123px; left: 0; width: 1200px; height: 465px;
    background: linear-gradient(180deg, var(--grey-photo-a) 0%, var(--grey-photo-b) 100%); }
  .hero-band { position: absolute; top: 588px; left: 0; width: 1200px; height: 86px; background: var(--black); }

  .plan-card { position: absolute; top: 588px; left: 176px; width: 846px; height: 106px; background: var(--white); padding: 7px 7px 0 7px; }
  .plan-card-inner { width: 100%; height: 99px; background: var(--nav); text-align: center; color: var(--white); padding-top: 23px; }
  .plan-title { font-family: "Cinzel", serif; font-weight: 400; font-size: 34px; line-height: 1; letter-spacing: 1.5px; }
  .plan-subtitle { font-size: 20.5px; margin-top: 3px; font-weight: 400; }

  .pillars { position: absolute; left: 0; top: 0; width: 1200px; }
  .pillar { position: absolute; left: 0; width: 1200px; }
  .pillar-icon { position: absolute; left: 216px; width: 54px; height: 54px; }
  .pillar-heading { position: absolute; left: 299px; font-family: "Cinzel", serif; font-weight: 600; font-size: 28px; color: var(--red); line-height: 1; }
  .pillar-text { position: absolute; left: 299px; width: 682px; font-size: 12.3px; line-height: 14.6px; }
  .pillar-text.small { font-size: 11px; line-height: 13.5px; width: 660px; }

  .site-footer { position: absolute; top: 1128px; left: 0; width: 1200px; height: 42px; background: var(--red-dark); color: var(--white); font-size: 11px; text-align: center; line-height: 42px; }
</style>
</head>
<body>
  <header class="site-header">
    <div class="brand">
      <span class="brand-mark"></span>
      <span class="brand-name">Halvern Strategy</span>
    </div>
  </header>

  <nav class="main-nav">
    <a class="is-active" href="#">HOME</a>
    <a href="#">ABOUT US</a>
    <a href="#">SPECIALISED PROJECTS</a>
    <a href="#">BUSINESS INTELLIGENCE</a>
    <a href="#">CONTACT US</a>
  </nav>

  <div class="hero" role="img" aria-label="Man seen from behind facing a wall of grey CCTV camera feeds of empty offices"></div>
  <div class="hero-band"></div>

  <section class="plan-card">
    <div class="plan-card-inner">
      <h1 class="plan-title">Strategic &amp; Operational Plan</h1>
      <p class="plan-subtitle">Our People and Our Proccesses are the difference!</p>
    </div>
  </section>

  <main class="pillars">
    <article class="pillar" style="top:739px">
      <svg class="pillar-icon" viewBox="0 0 54 54" aria-hidden="true">
        <g stroke="var(--red)" stroke-width="2.5" stroke-linecap="round">
          <line x1="27" y1="3" x2="27" y2="8"/><line x1="13" y1="8" x2="16" y2="12"/><line x1="41" y1="8" x2="38" y2="12"/>
          <line x1="5" y1="20" x2="10" y2="21"/><line x1="49" y1="20" x2="44" y2="21"/>
          <line x1="7" y1="32" x2="11" y2="30"/><line x1="47" y1="32" x2="43" y2="30"/>
        </g>
        <path d="M27 13a11 11 0 0 0-7 19.5c1.5 1.3 2 3 2 5h10c0-2 .5-3.7 2-5A11 11 0 0 0 27 13z" fill="none" stroke="var(--icon)" stroke-width="2.5"/>
        <rect x="22" y="39" width="10" height="3" fill="var(--icon)"/>
        <rect x="23" y="43" width="8" height="4" rx="1.5" fill="var(--icon)"/>
      </svg>
      <h2 class="pillar-heading" style="top:0">VISSION</h2>
      <p class="pillar-text" style="top:35px">We a united Halvern Strategy Team are committed to growing our people and refining our processes to take every Client from normal to excellent security, and we are focussed on building our Client base in diamonds and mining by one new Client per quarter.</p>
    </article>

    <article class="pillar" style="top:851px">
      <svg class="pillar-icon" viewBox="0 0 54 54" aria-hidden="true">
        <rect x="4" y="26" width="8" height="16" fill="var(--red)"/>
        <rect x="16" y="18" width="8" height="24" fill="var(--red)"/>
        <path d="M2 26 L8 19 L14 26 Z" fill="var(--red)"/>
        <path d="M14 18 L20 10 L26 18 Z" fill="var(--red)"/>
        <rect x="30" y="10" width="10" height="32" fill="var(--icon)"/>
        <rect x="2" y="44" width="50" height="4" fill="var(--icon)"/>
      </svg>
      <h2 class="pillar-heading" style="top:0">MISSION</h2>
      <p class="pillar-text" style="top:34px">As a Team we are committed to building mutual respect between each member and our Clients. Based on trust and discretion we design CCTV and electronic security that protects what matters most.</p>
    </article>

    <article class="pillar" style="top:971px">
      <svg class="pillar-icon" viewBox="0 0 54 54" aria-hidden="true">
        <circle cx="30" cy="32" r="14" fill="var(--white)" stroke="var(--red)" stroke-width="4"/>
        <line x1="30" y1="32" x2="30" y2="23" stroke="var(--red)" stroke-width="2.5" stroke-linecap="round"/>
        <line x1="30" y1="32" x2="36" y2="35" stroke="var(--red)" stroke-width="2.5" stroke-linecap="round"/>
        <rect x="10" y="14" width="6" height="30" fill="var(--icon)"/>
      </svg>
      <h2 class="pillar-heading" style="top:0">VALUES</h2>
      <p class="pillar-text small" style="top:35px">We a united Halvern Strategy Team value integrity, confidentiality and precision. Every security design is backed by business intelligence, tested against real risk and delivered with care for our Clients, their people and their assets.</p>
    </article>
  </main>

  <footer class="site-footer">© Copyright 2015, Halvern Strategy, Inc. All rights reserved.</footer>
</body>
</html>
```